Thriving Mexican import business needs a new business card

Need a refresher of our current business card. Looking for a lighter background with the logo on one side. We will want this file to be adjustable so we can change names, emails and mobile numbers.
We are open to ideas but maintaining a professional image is critical.
Thankyou,

Target Market(s)

Anyone in food industry

Industry/Entity Type

Wholesale

Contact Information for Business Card

Mark Vellanoweth
Director
Corvan Products & Liquor Pty Ltd
5B Larkfield Ct, Brimsworth VIC 3051
0491325067 (03) 95147286
mark@corvanimports.com.au
corvanimportedgoodsandspirits.com.au

Font styles to use
Serif
Other font styles liked:
• NeoGram Heavy

Requirements
Must have
• Professional yet memorable
Corvan logo
Nice to have
• Chilli or tequila/mexican food pictures
Should not have
• Dark background

```html
<!DOCTYPE html>
<html lang="en">
<head>
<meta charset="utf-8">
<title>Corvan Business Card</title>
<link rel="stylesheet" href="https://fonts.googleapis.com/css2?family=Oswald:wght@400;500;600&family=Roboto+Condensed:wght@400&family=Archivo:wght@600&family=Alfa+Slab+One&display=swap">
<style>
  :root {
    --backdrop: #ece6dc;
    --card-white: #ffffff;
    --ink: #111111;
    --accent: #d0663a;
    --terracotta: #d4683c;
    --bottle-amber: #c98a52;
    --plaque: #6b3a2c;
    --plaque-text: #ecc9b4;
    --tagline-light: #fbe9dd;
  }
  * { margin: 0; padding: 0; box-sizing: border-box; }
  html, body { width: 1200px; height: 859px; overflow: hidden; background: var(--backdrop); }
  .canvas { position: relative; width: 1200px; height: 859px; }

  .card { position: absolute; top: 289px; width: 501px; height: 285px; overflow: hidden;
          box-shadow: 0 4px 14px rgba(0,0,0,0.18); }
  .card-front { left: 60px; background: var(--card-white); }
  .card-back { left: 639px; background: var(--terracotta); }

  /* front */
  .brand-block { position: absolute; left: 50px; top: 80px; width: 140px; text-align: center; }
  .brand-square { display: block; width: 36px; height: 36px; margin: 0 auto; background: var(--ink); }
  .brand-name { margin-top: 24px; font-family: 'Oswald', sans-serif; font-weight: 600; font-size: 40px;
                line-height: 1; color: var(--ink); white-space: nowrap; }
  .brand-tagline { margin-top: 6px; font-family: 'Oswald', sans-serif; font-weight: 400; font-size: 10.5px;
                   line-height: 1; color: var(--ink); white-space: nowrap; letter-spacing: 0.1px; }
  .divider { position: absolute; left: 205px; width: 1.5px; background: var(--accent); }
  .divider.d1 { top: 78px; height: 28px; }
  .divider.d2 { top: 128px; height: 10px; }
  .divider.d3 { top: 160px; height: 47px; }
  .details { position: absolute; left: 225px; top: 76px; font-family: 'Roboto Condensed', sans-serif;
             font-size: 13px; color: var(--ink); }
  .person-name { font-family: 'Archivo', sans-serif; font-weight: 600; font-size: 17px;
                 color: var(--accent); letter-spacing: 0.4px; text-transform: uppercase; line-height: 1.2; }
  .person-role { margin-top: 1px; }
  .address { margin-top: 18px; }
  .contact-list { list-style: none; margin-top: 16px; }
  .contact-list li { display: flex; align-items: center; height: 18px; }
  .contact-list svg { width: 12px; height: 12px; margin-right: 8px; flex: none; }
  .sep { color: var(--accent); margin: 0 3px; }

  /* back */
  .ornament-area { position: absolute; left: 21px; top: 72px; width: 466px; height: 213px;
                   background: linear-gradient(180deg, rgba(240,170,130,0) 0%, rgba(240,170,130,0.35) 100%); }
  .product-photo { position: absolute; left: 127px; top: 0; width: 258px; height: 170px;
                   background: linear-gradient(180deg, rgba(120,80,60,0.55) 0%, rgba(201,138,82,0.6) 55%, rgba(212,104,60,0) 100%); }
  .back-name { position: absolute; left: 0; width: 100%; top: 92px; text-align: center;
               font-family: 'Oswald', sans-serif; font-weight: 600; font-size: 66px; line-height: 1;
               color: var(--card-white); }
  .back-tagline { position: absolute; left: 0; width: 100%; top: 174px; text-align: center;
                  font-family: 'Oswald', sans-serif; font-weight: 400; font-size: 15px; line-height: 1;
                  color: var(--tagline-light); white-space: nowrap; }
  .plaque { position: absolute; left: 148px; top: 203px; width: 204px; height: 64px; }
  .plaque-text { position: absolute; left: 148px; top: 203px; width: 204px; height: 64px;
                 display: flex; align-items: center; justify-content: center;
                 font-family: 'Alfa Slab One', serif; font-size: 21px; letter-spacing: 1px;
                 color: var(--plaque-text); }
</style>
</head>
<body>
<div class="canvas">
  <section class="card card-front">
    <div class="brand-block">
      <span class="brand-square"></span>
      <div class="brand-name">CORVAN</div>
      <div class="brand-tagline">MEXICAN PRODUCTS &amp; LIQUOR</div>
    </div>
    <span class="divider d1"></span>
    <span class="divider d2"></span>
    <span class="divider d3"></span>
    <div class="details">
      <div class="person-name">Mark Vellanoweth</div>
      <div class="person-role">Director</div>
      <div class="address">5B Larkfield Ct, Brimsworth VIC 3051</div>
      <ul class="contact-list">
        <li>
          <svg viewBox="0 0 12 12" fill="none" stroke="var(--accent)" stroke-width="1"><circle cx="6" cy="6" r="5.4"/><path d="M4 3.3l1 1.4-.6.7c.4.9 1 1.5 1.9 1.9l.7-.6 1.4 1-.6 1c-2.3-.3-4.1-2.1-4.4-4.4z"/></svg>
          <span>049 132 5067<span class="sep">|</span>(03) 9514 7286</span>
        </li>
        <li>
          <svg viewBox="0 0 12 12" fill="none" stroke="var(--accent)" stroke-width="1"><rect x="0.8" y="2.5" width="10.4" height="7"/><path d="M0.8 2.5l5.2 4 5.2-4"/></svg>
          <span>mark@corvanimports.com.au</span>
        </li>
        <li>
          <svg viewBox="0 0 12 12" fill="none" stroke="var(--accent)" stroke-width="0.9"><circle cx="6" cy="6" r="5.3"/><ellipse cx="6" cy="6" rx="2.3" ry="5.3"/><path d="M0.7 6h10.6M1.5 3.3h9M1.5 8.7h9"/></svg>
          <span>corvanimportedgoodsandspirits.com.au</span>
        </li>
      </ul>
    </div>
  </section>

  <section class="card card-back">
    <div class="ornament-area" role="img" aria-label="Mexican folk floral ornament with swirling vines and flowers"></div>
    <div class="product-photo" role="img" aria-label="Photograph of tequila bottles and Mexican products"></div>
    <div class="back-name">CORVAN</div>
    <div class="back-tagline">MEXICAN PRODUCTS &amp; LIQUOR</div>
    <svg class="plaque" viewBox="0 0 204 64">
      <path d="M14 4h176l10 10v36l-10 10H14L4 50V14z" fill="var(--plaque)" stroke="var(--plaque)" stroke-width="2"/>
      <path d="M17 9h170l8 8v30l-8 8H17l-8-8V17z" fill="none" stroke="var(--plaque-text)" stroke-opacity="0.35" stroke-width="1"/>
    </svg>
    <div class="plaque-text">TEQUILA</div>
  </section>
</div>
</body>
</html>
```